"Parker's True Grain Woodwork" with a logo of a saw blade and handplane combined

Need a business card logo with a saw blade and hand plane
combined with Parker's True Grain Woodwork on it, and a unique design.

Woodworking has been in my family for generations, from carpentry, to milling logs for old farm homes and barns in the 1930's and 1940's. My grandfather had a small carpentry business from his home,and passed his skills down to my father who also did woodworking from his own small business. Having the passion for woodwork in my blood, I'm trying to continue with my own small business doing custom fine woodwork such as tables, small cabinetry and even outdoor projects to suite the customers needs. All my projects start with a rough piece of lumber, what ever the species suited for the project, and is milled to dimensions , assembled, and finished all by hand for a true handcrafted project.

My target market would be people who want a custom handmade piece, something that they can't find in stores and is unique. Also people who are willing to pay and appreciate the value, which is sometimes a hard market to find.

As far as design, I think I would like to get a sleek looking saw blade on the card combined with a hand plane some how. Background colour maybe a dark wood texture or grey? Colours I like are grey, black, reds, white, yellows but depending on how the card is looking I'm not afraid to use a cool colour to make something stand out. Just want the card to flow ,look clean and unique. Lettering I like serif and script or something similar to these that looks good on the card.

Facebook page is under Parker's True Grain Woodwork
Updates

If I could get logo on the card, a saw blade, hand plane or combine both together would be nice! Added Saturday, June 11, 2016

Target Market(s)

People that like a unique hand made project built to last

Industry/Entity Type

Business

Contact Information for Business Card

Parkers True Grain Woodwork
Hand crafted by: Owen Parker
Phone: 905 618-2297
Address: 412 Birchview Rd. Niagara-On-The-Lake Ont.
Email: parkerstruegrain@mailbox-example.com
Facebook: Parkers True Grain Woodwork
prefer icons for the info!

Font styles to use
Serif
Script

Requirements
Must have
• Nice clean look, little bit bold with an elegant taste
• Prefer black lettering
Nice to have
• I like silver for the saw blade and silver with brown handles on the hand plane!
Should not have
• Bright colours

```html
<!DOCTYPE html>
<html lang="en">
<head>
<meta charset="utf-8">
<title>Parker's True Grain Woodwork – Business Card</title>
<link rel="stylesheet" href="https://fonts.googleapis.com/css2?family=Oswald:wght@500&family=Source+Sans+3:wght@400;600&display=swap">
<style>
  :root {
    --page-bg: #e6e2e0;
    --card-frost: #f6f2f1;
    --brand-brown: #6e4312;
    --text-dark: #3a2a1a;
    --silver-dark: #8c8c8c;
    --silver-mid: #c9c9c9;
    --silver-light: #ffffff;
    --ghost: rgba(110, 67, 18, 0.12);
  }
  * { box-sizing: border-box; margin: 0; padding: 0; }
  html, body { width: 1200px; height: 900px; overflow: hidden; }
  body {
    background: var(--page-bg);
    position: relative;
    font-family: "Source Sans 3", "Myriad Pro", sans-serif;
  }
  .card {
    position: absolute;
    width: 556px;
    height: 344px;
    background: var(--card-frost);
    overflow: hidden;
    box-shadow: 0 4px 14px rgba(0,0,0,0.12);
  }
  .card--front { left: 238px; top: 61px; }
  .card--back { left: 460px; top: 518px; }

  /* front */
  .brand-mark {
    position: absolute;
    left: 0; right: 0; top: 26px;
    display: flex; flex-direction: column; align-items: center;
  }
  .brand-mark__disc {
    width: 96px; height: 96px; border-radius: 50%;
    background: linear-gradient(180deg, var(--silver-dark), var(--silver-light) 55%, var(--silver-mid));
  }
  .brand-name {
    margin-top: 14px;
    font-family: "Oswald", "Arial Narrow", sans-serif;
    font-weight: 500;
    font-size: 25px;
    letter-spacing: 0.2px;
    color: var(--brand-brown);
    text-transform: uppercase;
    white-space: nowrap;
  }
  .contact-band {
    position: absolute;
    left: 0; right: 0; top: 193px; bottom: 0;
    background: linear-gradient(180deg,
      #8f8f8f 0%, #bdbdbd 14%, #e9e9e9 38%, #ffffff 58%,
      #dadada 74%, #a8a8a8 90%, #9a9a9a 100%);
  }
  .owner {
    position: absolute; right: 302px; top: 38px;
    text-align: right; color: var(--text-dark);
    white-space: nowrap;
  }
  .owner__name {
    font-size: 20px; font-weight: 600; color: var(--brand-brown);
    margin-bottom: 6px; line-height: 26px;
  }
  .owner__address { font-size: 15px; line-height: 20px; }
  .contact-list {
    position: absolute; left: 282px; top: 41px;
    list-style: none; color: var(--text-dark); font-size: 14px;
  }
  .contact-list li {
    display: flex; align-items: center; gap: 8px;
    height: 21px; line-height: 21px;
    white-space: nowrap;
  }
  .contact-list svg { width: 12px; height: 12px; fill: var(--brand-brown); flex: none; }
  .social {
    position: absolute; left: 282px; top: 93px;
    display: flex; align-items: center; gap: 8px;
    font-size: 13px; color: var(--text-dark);
    white-space: nowrap;
  }
  .social__dot {
    width: 31px; height: 31px; border-radius: 50%;
    background: var(--brand-brown); flex: none;
  }

  /* back */
  .ghost-name {
    position: absolute; left: 0; right: 0; top: 135px;
    text-align: center;
    font-family: "Oswald", "Arial Narrow", sans-serif;
    font-weight: 500; font-size: 25px;
    color: var(--ghost); text-transform: uppercase;
    white-space: nowrap;
  }
  .back-band {
    position: absolute; left: 0; right: 0; top: 187px; bottom: 0;
    background: var(--brand-brown);
    display: flex; align-items: center; justify-content: center; gap: 18px;
  }
  .back-band__disc {
    width: 64px; height: 64px; border-radius: 50%; background: #ffffff;
  }
  .back-band__name {
    font-family: "Oswald", "Arial Narrow", sans-serif;
    font-weight: 500; font-size: 26px;
    color: #ffffff; text-transform: uppercase;
    white-space: nowrap;
  }
</style>
</head>
<body>

<section class="card card--front" aria-label="Business card front">
  <div class="brand-mark">
    <div class="brand-mark__disc"></div>
    <h1 class="brand-name">Parker's True Grain Woodwork</h1>
  </div>

  <div class="contact-band">
    <div class="owner">
      <p class="owner__name">Owen Parker</p>
      <p class="owner__address">412 Birchview Rd. Niagara<br>On-The-Lake Ont.</p>
    </div>

    <ul class="contact-list">
      <li>
        <svg viewBox="0 0 24 24" aria-hidden="true"><path d="M6.6 10.8a15.1 15.1 0 0 0 6.6 6.6l2.2-2.2c.3-.3.7-.4 1-.2 1.1.4 2.3.6 3.6.6.6 0 1 .4 1 1V20c0 .6-.4 1-1 1A17 17 0 0 1 3 4c0-.6.4-1 1-1h3.5c.6 0 1 .4 1 1 0 1.3.2 2.5.6 3.6.1.3 0 .7-.2 1z"/></svg>
        <span>905 618-2297</span>
      </li>
      <li>
        <svg viewBox="0 0 24 24" aria-hidden="true"><path d="M2 5h20v14H2z M3 6l9 7 9-7" /></svg>
        <span>parkerstruegrain@mailbox-example.com</span>
      </li>
    </ul>

    <div class="social">
      <span class="social__dot"></span>
      <span>Parkers True Grain Woodwork</span>
    </div>
  </div>
</section>

<section class="card card--back" aria-label="Business card back">
  <p class="ghost-name">Parker's True Grain Woodwork</p>
  <div class="back-band">
    <span class="back-band__disc"></span>
    <span class="back-band__name">Parker's True Grain</span>
  </div>
</section>

</body>
</html>
```